Roofing Company Sales Rep Business Card

Business card for sales rep to canvass and hand out to property owners/managers for free roof inspections and roof replacements.

```html
<!DOCTYPE html>
<html lang="en">
<head>
<meta charset="utf-8">
<title>Ridgeline Roofing – Business Card</title>
<link rel="stylesheet" href="https://fonts.googleapis.com/css2?family=Poppins:wght@400;600;700&display=swap">
<style>
  :root {
    --page-bg: #e6e2e2;
    --card-bg: #f6f3f3;
    --brand-red: #e30000;
    --ink: #141414;
    --text: #1c1c1c;
  }
  * { box-sizing: border-box; margin: 0; padding: 0; }
  html, body {
    width: 1200px; height: 900px; overflow: hidden;
    background: var(--page-bg);
    font-family: "Poppins", sans-serif;
  }
  .card {
    position: absolute; left: 75px; top: 125px;
    width: 1050px; height: 650px;
    background: linear-gradient(135deg, #faf8f8 0%, var(--card-bg) 55%, #eee9e9 100%);
    box-shadow: 0 18px 40px rgba(0,0,0,0.18);
    overflow: hidden;
  }
  .brand {
    position: absolute; left: 40px; top: 250px; width: 470px;
    display: flex; align-items: center; justify-content: center; gap: 14px;
  }
  .brand-mark { width: 26px; height: 26px; background: var(--brand-red); flex: none; }
  .brand-name {
    font-weight: 700; font-size: 38px; letter-spacing: 1px;
    color: var(--ink); text-transform: uppercase; white-space: nowrap;
  }
  .contact-block { position: absolute; left: 548px; top: 96px; color: var(--text); }
  .person-name { font-weight: 600; font-size: 42px; line-height: 1.1; letter-spacing: 0.5px; }
  .person-name .first { color: var(--brand-red); }
  .person-name .last { color: var(--ink); }
  .person-role { font-size: 29px; line-height: 1.2; }
  .contact-list { list-style: none; margin-top: 30px; }
  .contact-list li {
    display: flex; align-items: center; gap: 10px;
    font-size: 29px; line-height: 39px;
  }
  .contact-list svg { width: 28px; height: 28px; flex: none; fill: var(--brand-red); }
  .address { margin-top: 26px; font-size: 29px; line-height: 39px; padding-left: 2px; }
  .tagline {
    position: absolute; left: 0; right: 0; top: 472px; text-align: center;
    font-weight: 700; font-size: 31px; color: var(--ink);
  }
  .tagline .highlight { color: var(--brand-red); }
  .footer-rule {
    position: absolute; left: 0; right: 0; top: 574px; height: 6px;
    background: var(--ink);
  }
  .footer-band {
    position: absolute; left: 0; right: 0; top: 588px; bottom: 0;
    background: var(--brand-red);
  }
</style>
</head>
<body>
  <div class="card">
    <div class="brand">
      <span class="brand-mark"></span>
      <span class="brand-name">Ridgeline Roofing</span>
    </div>

    <div class="contact-block">
      <h1 class="person-name"><span class="first">DANIEL</span> <span class="last">HARPER</span></h1>
      <p class="person-role">Managing Director</p>
      <ul class="contact-list">
        <li>
          <svg viewBox="0 0 24 24"><path d="M6.6 10.8a15 15 0 0 0 6.6 6.6l2.2-2.2a1 1 0 0 1 1-.25 11.4 11.4 0 0 0 3.6.57 1 1 0 0 1 1 1V20a1 1 0 0 1-1 1A17 17 0 0 1 3 4a1 1 0 0 1 1-1h3.5a1 1 0 0 1 1 1c0 1.25.2 2.45.57 3.6a1 1 0 0 1-.25 1z"/></svg>
          055-987 654 321
        </li>
        <li>
          <svg viewBox="0 0 24 24"><path d="M2 5h20v14H2z"/><path d="M3 6l9 7 9-7" fill="none" stroke="#fff" stroke-width="1.6"/></svg>
          hello@ridgelineroof.com
        </li>
        <li>
          <svg viewBox="0 0 24 24"><path d="M12 2a10 10 0 1 0 0 20 10 10 0 0 0 0-20zm6.9 6h-3a15 15 0 0 0-1.3-3.9A8 8 0 0 1 18.9 8zM12 4c.9 1.2 1.6 2.6 2 4h-4c.4-1.4 1.1-2.8 2-4zM4.3 14a8 8 0 0 1 0-4h3.3a16 16 0 0 0 0 4zm.8 2h3a15 15 0 0 0 1.3 3.9A8 8 0 0 1 5.1 16zm3-8h-3a8 8 0 0 1 4.3-3.9A15 15 0 0 0 8.1 8zM12 20c-.9-1.2-1.6-2.6-2-4h4c-.4 1.4-1.1 2.8-2 4zm2.4-6H9.6a14 14 0 0 1 0-4h4.8a14 14 0 0 1 0 4zm.2 5.9a15 15 0 0 0 1.3-3.9h3a8 8 0 0 1-4.3 3.9zm1.8-5.9a16 16 0 0 0 0-4h3.3a8 8 0 0 1 0 4z"/></svg>
          www.ridgelineroof.com
        </li>
      </ul>
      <p class="address">318, Cedar Hollow Avenue<br>Westbrook 40218, Country</p>
    </div>

    <p class="tagline"><span class="highlight">FREE Roof Inspections</span> and Roof Replacements</p>

    <div class="footer-rule"></div>
    <div class="footer-band"></div>
  </div>
</body>
</html>
```